Torven Medical needs bold attention catching website for healthcare professionals(target)

I need a hero page as well as a products and about page for a website of mine. I specialize in orthopedic instruments . Specifically bone drills and saws. This whole company was founded to bring superb quality highly discounted medical instruments. Specifically bone drills, bone saws, k-wires and pins. Two main points should be cost savings and superior quality.

Target Market(s)

healthcare professionals Surgeons and hospital material managers

Number of Pages Required

3 page

Font styles to use
Serif

Colors

Designer to choose colors to be used in the design.

Requirements
Must have
• colors should match logo design

```html
<!DOCTYPE html>
<html lang="en">
<head>
<meta charset="utf-8">
<title>Torven Medical – Orthopedic Medical Devices</title>
<link rel="stylesheet" href="https://fonts.googleapis.com/css2?family=Alegreya:wght@400;500;700;800&display=swap">
<style>
  :root{
    --orange:#f7941d;
    --blue:#4a7ab8;
    --steel:#4f86b0;
    --teal:#5a95a6;
    --ink:#1f1f1f;
    --text:#4a4a4a;
    --footer:#151515;
    --white:#ffffff;
  }
  *{box-sizing:border-box;margin:0;padding:0}
  html,body{width:1200px;height:2732px;overflow:hidden}
  body{position:relative;background:var(--white);font-family:"Alegreya",Georgia,serif;color:var(--ink)}
  .abs{position:absolute}
  .center{left:0;width:1200px;text-align:center}

  /* header */
  .site-header{top:0;left:0;width:1200px;height:91px;background:var(--white)}
  .brand{left:160px;top:30px;font-size:26px;font-weight:500;color:var(--ink);display:flex;align-items:center;gap:10px}
  .brand-dot{width:14px;height:14px;border-radius:50%;background:var(--orange)}
  .nav a{position:absolute;top:38px;font-size:12px;font-weight:700;letter-spacing:.5px;color:var(--ink);text-decoration:none}
  .nav .active{color:var(--orange);border-bottom:2px solid var(--orange);padding:0 4px 4px}

  /* hero */
  .hero{top:91px;left:0;width:1200px;height:524px;background:linear-gradient(100deg,#e9c99a 0%,#ece2d6 30%,#e6e8ec 60%,#c8d4e2 85%,#4d78ad 100%)}
  .hero-veil{top:91px;left:0;width:1200px;height:524px;background:rgba(255,255,255,.35)}
  .hero-title{top:231px;font-size:36px;font-weight:800;letter-spacing:.5px;color:#222}
  .hero-sub{top:314px;font-size:25px;font-weight:500;line-height:37px;color:#444}
  .btn{display:flex;align-items:center;justify-content:center;border-radius:22px;font-size:12px;font-weight:700;letter-spacing:1.5px;text-transform:uppercase}
  .btn-solid{background:var(--orange);color:var(--white)}
  .btn-line{border:2px solid var(--orange);color:var(--orange)}

  /* why */
  .section-title{font-size:26px;font-weight:700;letter-spacing:.5px;color:var(--ink)}
  .section-title span{border-bottom:2px solid var(--orange);padding-bottom:1px}
  .feature{width:200px;text-align:center}
  .feature svg{display:block;margin:0 auto}
  .feature h3{margin-top:12px;font-size:18px;font-weight:700;color:#333}
  .feature p{margin-top:18px;font-size:13px;line-height:15px;color:#555}
  .feature .pill{margin:18px auto 0;width:128px;height:32px;border-radius:16px;color:var(--white);font-size:10px;font-weight:700;letter-spacing:1px;display:flex;align-items:center;justify-content:center}

  /* about */
  .about-bg{top:1159px;left:0;width:1200px;height:433px;background:linear-gradient(90deg,#eef1f6 0%,#e3e8f0 55%,#b9c8dc 80%,#6f8fc5 92%,#e8ecf2 100%)}
  .about-veil{top:1159px;left:0;width:1200px;height:433px;background:rgba(236,240,246,.55)}
  .about-text{top:1320px;left:240px;width:720px;text-align:center;font-size:15px;line-height:22.5px;color:#555}

  /* products */
  .products-img{top:1592px;left:603px;width:597px;height:491px;background:linear-gradient(125deg,#f3f5f8 0%,#dfe7ef 35%,#f6b26a 55%,#cfd9e4 70%,#f4f6f9 100%)}
  .products-text{top:1789px;left:161px;width:400px;font-size:15px;line-height:22.5px;color:#444}

  /* contact */
  .contact-bg{top:2083px;left:0;width:1200px;height:442px;background:linear-gradient(180deg,#e8e8e8 0%,#dcdcdc 55%,#b5b5b5 100%)}
  .field{border:1px solid #333;background:transparent;font-size:12px;color:#555;padding:20px 0 0 22px;font-family:inherit}
  .send{top:2381px;left:160px;width:878px;height:48px;background:var(--ink);color:var(--white);font-size:12px;font-weight:700;letter-spacing:1.5px;display:flex;align-items:center;justify-content:center;border-radius:2px}

  /* footer */
  .site-footer{top:2525px;left:0;width:1200px;height:207px;background:var(--footer)}
  .foot-head{font-size:12px;font-weight:700;letter-spacing:.5px;color:var(--white)}
  .foot-link{font-size:10px;font-weight:700;color:var(--white);letter-spacing:.3px}
  .foot-social{left:958px;width:80px;display:flex;justify-content:space-between;align-items:center;font-size:10px;font-weight:700;color:var(--white)}
  .foot-social i{width:9px;height:9px;border-radius:50%;background:var(--white);display:block}
  .foot-brand{top:2604px;left:0;width:1200px;text-align:center;font-size:20px;font-weight:500;color:var(--white)}
  .foot-rule{top:2695px;left:160px;width:878px;height:1px;background:#555}
  .legal{top:2709px;font-size:8px;color:#ccc}
</style>
</head>
<body>

<header class="abs site-header">
  <div class="abs brand"><span class="brand-dot"></span>Torven Medical</div>
  <nav class="nav">
    <a class="active" style="left:548px">HOME</a>
    <a style="left:672px">PRODUCTS &#8964;</a>
    <a style="left:819px">ABOUT US</a>
    <a style="left:961px">CONTACT US</a>
  </nav>
</header>

<section>
  <div class="abs hero" role="img" aria-label="Doctors reviewing a tablet and clipboard in a bright clinic"></div>
  <div class="abs hero-veil"></div>
  <h1 class="abs center hero-title">HIGH QUALITY ORTHOPEDIC MEDICAL DEVICE</h1>
  <p class="abs center hero-sub">Torven Medical Company was founded to bring<br>superb quality highly discounted medical instruments.</p>
  <a class="abs btn btn-solid" style="top:450px;left:442px;width:150px;height:40px">View Products</a>
  <a class="abs btn btn-line" style="top:450px;left:608px;width:149px;height:40px">Learn More</a>
</section>

<section>
  <h2 class="abs center section-title" style="top:682px">WHY <span>TORVEN MEDICAL</span></h2>

  <div class="abs feature" style="left:147px;top:783px">
    <svg width="128" height="141" viewBox="0 0 128 141">
      <polygon points="64,2 124,36 124,105 64,139 4,105 4,36" fill="var(--blue)" stroke="#dde3ea" stroke-width="4"/>
      <circle cx="64" cy="58" r="26" fill="#fff"/>
      <polygon points="50,76 50,108 64,98 78,108 78,76" fill="#fff"/>
      <text x="64" y="59" text-anchor="middle" font-family="Alegreya,serif" font-size="12" font-weight="700" fill="var(--blue)">HIGH</text>
      <text x="64" y="70" text-anchor="middle" font-family="Alegreya,serif" font-size="7" fill="var(--blue)">QUALITY</text>
    </svg>
    <h3>High Quality</h3>
    <p>Torven Medical offers high quality products to the hospitals and...</p>
    <div class="pill" style="background:var(--blue)">MORE INFO</div>
  </div>

  <div class="abs feature" style="left:382px;top:783px">
    <svg width="128" height="141" viewBox="0 0 128 141">
      <polygon points="64,2 124,36 124,105 64,139 4,105 4,36" fill="var(--steel)" stroke="#dde3ea" stroke-width="4"/>
      <rect x="26" y="50" width="76" height="40" fill="none" stroke="#fff" stroke-width="4"/>
      <circle cx="64" cy="70" r="13" fill="none" stroke="#fff" stroke-width="3"/>
      <text x="64" y="76" text-anchor="middle" font-family="Alegreya,serif" font-size="16" font-weight="700" fill="#fff">$</text>
      <path d="M32,56 h8 M32,56 v8 M96,84 h-8 M96,84 v-8" stroke="#fff" stroke-width="3"/>
    </svg>
    <h3>Lower Cost</h3>
    <p>Torven Medical has been able to pass along cost savings of up...</p>
    <div class="pill" style="background:var(--steel)">MORE INFO</div>
  </div>

  <div class="abs feature" style="left:617px;top:783px">
    <svg width="128" height="141" viewBox="0 0 128 141">
      <polygon points="64,2 124,36 124,105 64,139 4,105 4,36" fill="var(--orange)" stroke="#dde3ea" stroke-width="4"/>
      <polygon points="60,56 86,56 86,46 102,62 86,78 86,68 60,68" fill="#fff"/>
      <polygon points="68,72 42,72 42,62 26,78 42,94 42,84 68,84" fill="#fff"/>
    </svg>
    <h3>Works Directly</h3>
    <p>Torven Medical works directly with hospital administrators...</p>
    <div class="pill" style="background:var(--steel)">MORE INFO</div>
  </div>

  <div class="abs feature" style="left:852px;top:783px">
    <svg width="128" height="141" viewBox="0 0 128 141">
      <polygon points="64,2 124,36 124,105 64,139 4,105 4,36" fill="var(--teal)" stroke="#dde3ea" stroke-width="4"/>
      <polygon points="38,54 50,44 78,44 90,54 90,92 38,92" fill="#fff"/>
      <rect x="38" y="62" width="52" height="3" fill="var(--teal)"/>
      <polygon points="56,44 72,44 72,66 64,60 56,66" fill="var(--teal)"/>
      <rect x="74" y="80" width="10" height="4" fill="var(--teal)"/>
    </svg>
    <h3>Generic Products</h3>
    <p>Torven Medical focus is on the orthopedic disposable market...</p>
    <div class="pill" style="background:var(--teal)">MORE INFO</div>
  </div>
</section>

<section>
  <div class="abs about-bg" role="img" aria-label="Surgeon in scrubs and cap standing in an operating room"></div>
  <div class="abs about-veil"></div>
  <h2 class="abs center section-title" style="top:1226px">ABOUT <span>TORVEN MEDICAL</span></h2>
  <p class="abs about-text">Torven Medical focus is on the orthopedic disposable market by providing quality generic products that are utilized to replace many legacy products that have low physician preference and are subject to 5%-10% annual unsustainable price increases...</p>
  <a class="abs btn btn-solid" style="top:1446px;left:506px;width:187px;height:40px">Read More</a>
</section>

<section>
  <h2 class="abs section-title" style="top:1658px;left:161px">PRODUCTS OF <span>TORVEN MEDICAL</span></h2>
  <p class="abs products-text">Lorem ipsum dolor sit amet, consectetur adipiscing elit, sed do eiusmod tempor incididunt ut labore et dolore magna aliqua. Ut enim ad minim veniam, quis nostrud exercitation ullamco... laboris nisi ut aliquip ex ea commodo consequat. Duis aute irure dolor in reprehenderit in voluptate...</p>
  <a class="abs btn btn-solid" style="top:1940px;left:161px;width:203px;height:40px">View Products</a>
  <div class="abs products-img" role="img" aria-label="Two bone drill bits standing on a white and orange geometric backdrop"></div>
</section>

<section>
  <div class="abs contact-bg" role="img" aria-label="Faded city street scene in grey tones"></div>
  <h2 class="abs center section-title" style="top:2151px">CONTACT US</h2>
  <p class="abs center" style="top:2189px;font-size:15px;color:#444">Lorem ipsum dolor sit amet, consectetur adipiscing elit, sed do eiusmod tempor incididunt ut.</p>
  <div class="abs field" style="top:2252px;left:160px;width:286px;height:45px">Name</div>
  <div class="abs field" style="top:2252px;left:456px;width:286px;height:45px">Email</div>
  <div class="abs field" style="top:2252px;left:752px;width:286px;height:45px">Phone</div>
  <div class="abs field" style="top:2308px;left:160px;width:878px;height:57px">Message</div>
  <div class="abs send">SEND</div>
</section>

<footer class="abs site-footer" role="img" aria-label="Dark street scene with people walking"></footer>
<div class="abs foot-head" style="top:2563px;left:160px">QUICK LINKS</div>
<div class="abs foot-link" style="top:2593px;left:160px">HOME</div>
<div class="abs foot-link" style="top:2616px;left:160px">PRODUCTS</div>
<div class="abs foot-link" style="top:2638px;left:160px">ABOUT US</div>
<div class="abs foot-link" style="top:2660px;left:160px">CONTACT US</div>
<div class="abs foot-brand">Torven Medical</div>
<div class="abs foot-head" style="top:2563px;left:958px">FOLLOW US</div>
<div class="abs foot-social" style="top:2593px">Friendsnet<i></i></div>
<div class="abs foot-social" style="top:2627px">Chirper<i></i></div>
<div class="abs foot-social" style="top:2661px">Snapgram<i></i></div>
<div class="abs foot-rule"></div>
<div class="abs legal" style="left:160px">Copyright @ Torven Medical. 2019 All Right Reserved.</div>
<div class="abs legal" style="left:903px;font-weight:700;color:#fff">Terms of Use &nbsp;|&nbsp; Privacy Policy</div>

</body>
</html>
```